Lorna and Vikram Destination Wedding Invitation

THE DESIGN
- We need a unique, fun and colourful wedding invitation.
- We would like the designs to be printed using letterpress (not block) and or laser cut. Open to suggestions.
- We would like to include the attached wedding logo.
- We would like a design that is fun yet classy.
- 3D if possible.
- Main colour: deep purple; secondary colour: green.

Colour example:
http://www.bloomvowshop.com/Soft-Petal-Marigold-Sprays-Posyp/mkrtz412.htm
- we did think about using the following product to enclose the necessary cards. This is not mandatory. http://www.vowsandtiesstore.co.uk/product/willow-fold-invitation#colour=19

TO AVOID
- Paisleys
- Obvious flowers
- Block letterpress

FAVOURED DESIGNS
http://i0.wp.com/www.inkmorrow.com/images/blog-images/cedar-lantern1.jpg?resize=400%2C533
http://studioferlune.com/collection-corvane.html
http://studioferlune.com/collection-baldric.html
https://www.craftlymart.com/listing/847362915/fougere-wedding-invitation-laser-cut

THE COUPLE
- Bride: Lorna Maeve Castellanos
- Groom: Vikram Dalbeth
- Both from Sydney, Australia
- Both living in London, UK
- Website: lornaandvikram.com

THE WEDDING:
- We are getting married in Koh Samui, Thailand, early next year.
- We have 3 official events, the welcome drinks (March 25), the wedding (March 27) and beach bbq (March 28).

THE INVITE -1 CARD design
For everyone, a page/card that will include the following:
- Reception/ Main invite
- Location card (Direction/Map). Venue: Tharuvan Cove Spa Resort
- RSVP - via website
See wording attachment for details.

I need an insert (template) for the following: - 1 design only.
- Tide Lantern Night
- Tots Hollow (for people with children)
- Rehearsal

ADDITIONAL
- We would like the design to be adaptable for place cards and or wedding programs (normal printer).

Please let me know if you need more information.

Target Market(s)

Fun, casual, unique

Industry/Entity Type

Wedding

Colors
6b449b
876aae
b7a5cd

Requirements
Must have
• Wedding logo
Nice to have
• Please see project description
Should not have

```html
<!DOCTYPE html>
<html lang="en">
<head>
<meta charset="utf-8">
<title>Lorna &amp; Vikram – Wedding Invitation</title>
<link rel="stylesheet" href="https://fonts.googleapis.com/css2?family=Oswald:wght@300;400&family=Parisienne&family=Sacramento&display=swap">
<style>
  :root {
    --purple: #6b449b;
    --purple-mid: #876aae;
    --purple-soft: #b7a5cd;
    --green: #2f7a4a;
    --sage: #8aa98a;
    --paper: #f7f4ec;
    --stripe: #efebe1;
    --dots: #a9a59a;
    --lotus-faint: #e4dce8;
  }
  * { box-sizing: border-box; margin: 0; padding: 0; }
  html, body { width: 851px; height: 1200px; overflow: hidden; background: #ffffff; }
  .invitation {
    position: relative;
    width: 851px;
    height: 1200px;
    background:
      repeating-linear-gradient(90deg, var(--paper) 0 6px, var(--stripe) 6px 7px);
  }
  .frame {
    position: absolute;
    left: 24px; right: 24px; top: 20px; bottom: 20px;
    border-left: 6px solid var(--purple);
    border-right: 6px solid var(--purple);
  }
  .lace-band {
    position: absolute;
    left: 24px; right: 24px;
    height: 70px;
    background: linear-gradient(var(--purple), var(--purple-mid));
  }
  .lace-band--top { top: 0; }
  .lace-band--bottom { bottom: 0; height: 90px; background: linear-gradient(var(--purple-mid), var(--purple)); }

  .monogram {
    position: absolute;
    top: 170px; left: 0; right: 0;
    text-align: center;
    font-family: "Oswald", sans-serif;
    font-weight: 400;
    font-size: 40px;
    letter-spacing: 4px;
    color: var(--purple);
  }
  .monogram::before {
    content: "";
    display: inline-block;
    width: 14px; height: 14px;
    border-radius: 50%;
    background: var(--purple);
    margin-right: 14px;
    vertical-align: middle;
  }

  .tagline {
    position: absolute;
    top: 410px; left: 0; right: 0;
    text-align: center;
    font-family: "Parisienne", cursive;
    font-size: 52px;
    color: var(--green);
  }
  .dotted-rule {
    position: absolute;
    left: 195px; right: 195px;
    height: 0;
    border-top: 3px dotted var(--dots);
  }
  .dotted-rule--thin { border-top-width: 2px; border-top-color: var(--purple-soft); }

  .couple {
    position: absolute;
    top: 540px; left: 0; right: 0;
    height: 190px;
    text-align: center;
  }
  .couple__amp {
    position: absolute;
    left: 0; right: 0; top: -30px;
    font-family: "Oswald", sans-serif;
    font-weight: 300;
    font-size: 230px;
    line-height: 1;
    color: var(--sage);
    opacity: 0.85;
  }
  .couple__names {
    position: absolute;
    left: 0; right: 0; top: 45px;
    font-family: "Oswald", sans-serif;
    font-weight: 400;
    font-size: 82px;
    letter-spacing: 1px;
    line-height: 1;
    color: var(--green);
  }
  .couple__names span { display: inline-block; }
  .couple__names .gap { width: 95px; }

  .invite-line {
    position: absolute;
    top: 808px; left: 0; right: 0;
    text-align: center;
    font-family: "Oswald", sans-serif;
    font-weight: 400;
    font-size: 27px;
    letter-spacing: 0.5px;
    color: var(--purple);
  }
  .date {
    position: absolute;
    top: 848px; left: 0; right: 0;
    text-align: center;
    font-family: "Sacramento", cursive;
    font-size: 66px;
    line-height: 1;
    color: var(--purple);
  }
  .faint-monogram {
    position: absolute;
    top: 990px; left: 0; right: 0;
    text-align: center;
    font-family: "Oswald", sans-serif;
    font-weight: 400;
    font-size: 40px;
    letter-spacing: 4px;
    color: var(--lotus-faint);
  }
</style>
</head>
<body>
<main class="invitation">
  <div class="lace-band lace-band--top" role="img" aria-label="Purple lace border pattern"></div>
  <div class="frame"></div>

  <div class="monogram">Lorna &amp; Vikram</div>

  <p class="tagline">.Our wedding day.</p>
  <div class="dotted-rule" style="top:492px"></div>
  <div class="dotted-rule" style="top:506px"></div>

  <div class="couple">
    <div class="couple__amp">&amp;</div>
    <h1 class="couple__names"><span>VIKRAM</span><span class="gap"></span><span>LORNA</span></h1>
  </div>

  <div class="dotted-rule" style="top:712px"></div>
  <div class="dotted-rule" style="top:726px"></div>

  <p class="invite-line">YOU ARE INVITED TO OUR WEDDING</p>
  <div class="dotted-rule dotted-rule--thin" style="top:846px"></div>
  <p class="date">27th march 2016</p>
  <div class="dotted-rule dotted-rule--thin" style="top:916px"></div>

  <div class="faint-monogram">Lorna &amp; Vikram</div>

  <div class="lace-band lace-band--bottom" role="img" aria-label="Purple lace border pattern"></div>
</main>
</body>
</html>
```